Design some Business Cards for Narvel Solutions

Please create some double sided business card designs for Narvel Solutions.They will be printed by pelk so please ensure that their guidelines are followed:

http://uk.pelkprint-example.com/help/faq/using-my-own-artwork.html

What we do and are about can be found on our website:

http://www.narvelsol-example.com.au.

Please ensure that you include an area for the following details:
- Name
- title
- email
- Mobile (cell phone)
- Web url

Please provide a photoshop compatible file that can be modified to cater for different staff. We will save the final file with our details and names etc. as a jpeg to suit the printers requirements.

(A photoshop version of our logo can be found attached. Please ensure it is used.)

```html
<!DOCTYPE html>
<html lang="en">
<head>
<meta charset="utf-8">
<title>Narvel Solutions – Business Cards</title>
<link rel="stylesheet" href="https://fonts.googleapis.com/css2?family=Open+Sans:wght@400;600;700&display=swap">
<style>
  :root {
    --page-bg: #d9dadb;
    --card-bg: #f7f7f5;
    --brand-blue: #1e8fe1;
    --brand-purple: #5b3a9a;
    --ink-dark: #2d2d2d;
    --ink-grey: #8a8a8a;
    --card-shadow: 0 6px 18px rgba(0,0,0,0.18);
  }
  * { box-sizing: border-box; margin: 0; padding: 0; }
  html, body { width: 1200px; height: 1200px; overflow: hidden; }
  body {
    background: var(--page-bg);
    font-family: "Open Sans", sans-serif;
    position: relative;
  }
  .card {
    position: absolute;
    left: 220px;
    width: 760px;
    height: 434px;
    background: var(--card-bg);
    box-shadow: var(--card-shadow);
  }
  .card--back { top: 110px; }
  .card--front { top: 656px; }

  .brand {
    display: flex;
    align-items: center;
    gap: 16px;
  }
  .brand__dot {
    width: 46px;
    height: 46px;
    border-radius: 50%;
    background: var(--brand-purple);
    flex: none;
  }
  .brand__name {
    color: var(--brand-blue);
    font-weight: 700;
    font-size: 44px;
    letter-spacing: 0.5px;
    white-space: nowrap;
  }

  .card--back .brand {
    position: absolute;
    left: 48px;
    top: 48px;
  }
  .card--back .brand__dot { width: 38px; height: 38px; }
  .card--back .brand__name { font-size: 36px; }

  .card--front .brand {
    position: absolute;
    left: 50%;
    top: 50%;
    transform: translate(-50%, -50%);
  }

  .person {
    position: absolute;
    left: 430px;
    top: 176px;
  }
  .person__name {
    font-size: 26px;
    color: var(--ink-dark);
    font-weight: 400;
  }
  .person__surname { color: var(--ink-grey); }
  .person__title {
    font-size: 16px;
    color: var(--ink-grey);
    margin-top: 2px;
  }
  .contact {
    list-style: none;
    margin-top: 24px;
    font-size: 15px;
    color: var(--ink-grey);
    line-height: 1.9;
  }
</style>
</head>
<body>
  <section class="card card--back" aria-label="Business card, details side">
    <div class="brand">
      <span class="brand__dot"></span>
      <span class="brand__name">Narvel Solutions</span>
    </div>
    <div class="person">
      <p class="person__name">Idris <span class="person__surname">FALKNER</span></p>
      <p class="person__title">Graphic Designer</p>
      <ul class="contact">
        <li>+61 400 555 019</li>
        <li>enquire@narvelsol-example.com.au</li>
        <li>www.narvelsol-example.com.au</li>
      </ul>
    </div>
  </section>

  <section class="card card--front" aria-label="Business card, logo side">
    <div class="brand">
      <span class="brand__dot"></span>
      <span class="brand__name">Narvel Solutions</span>
    </div>
  </section>
</body>
</html>
```